Sam Greenfield Billboard

**Task Description: Billboard Design for Self Storage Facility**

**Objective:**
Design a captivating billboard to promote our self-storage facility with a focus on our convenient location and online rental capabilities.

**Key Messages to Include:**
1. **Location Emphasis:** Highlight that our facility is located right beside the billboard (maybe by using an arrow pointing left).
2. **Online Rental Convenience:** Feature prominently that customers can "Rent Online Anytime!” or that we are "Always Open Online!"

**Target Audience:**
- Local residents looking for convenient self-storage solutions.
- Businesses needing storage space accessible around the clock.

**Design Elements:**
1. **Visual Impact:** Eye-catching graphics and colors that stand out against the surroundings.
2. **Clear Text:** Bold and concise messaging that can be read and understood quickly.
3. **Contact Information:** Include our phone number and website URL for easy access to further information.

**Additional Information:**
- Billboard dimensions: 12 ft. x 24 ft.
- Preferred color scheme: Bright and attention-grabbing, but professional.
- Branding: Incorporate our logo and brand colors to maintain consistency.

**Deliverables:**
- High-resolution digital file compatible with billboard printing specifications.
- Consider mockups or visualizations for presentation purposes.

Please note that I have attached current logos/graphics that we would love to incorporate into the billboard as well as a picture of our current billboard. Our logo (Sam Greenfield Self Storage - SG navy.png) MUST be incorporated into the billboard. Also feel free to add any of the current descriptions from the picture of our current billboard into the design. Instead of using "Climate Controlled" use "Temperature Controlled". Thank you for your attention to these details. We look forward to reviewing your proposed design!

```html
<!DOCTYPE html>
<html lang="en">
<head>
<meta charset="utf-8">
<title>Sam Greenfield Billboard</title>
<link rel="stylesheet" href="https://fonts.googleapis.com/css2?family=Montserrat:wght@800&family=Fredoka:wght@600&family=Lilita+One&family=Oswald:wght@700&display=swap">
<style>
  :root{
    --page:#4a4a4c;
    --navy:#1f2d5c;
    --navy-deep:#16214a;
    --red:#c3161c;
    --green:#5cb82e;
    --green-light:#8ed653;
    --pill-dark:#3d3f42;
    --white:#ffffff;
    --photo-light:#f1f2f1;
    --photo-mid:#dcd8cf;
    --photo-dark:#c9c2b4;
  }
  *{margin:0;padding:0;box-sizing:border-box}
  html,body{width:1200px;height:1200px;overflow:hidden;background:var(--page)}
  .billboard{position:absolute;left:40px;top:320px;width:1120px;height:560px;overflow:hidden;background:var(--photo-light)}
  .billboard__photo{position:absolute;inset:0;background:
      radial-gradient(ellipse at 40% 75%, var(--photo-dark) 0%, transparent 60%),
      linear-gradient(180deg, var(--photo-light) 0%, var(--photo-mid) 100%)}
  .billboard__shapes{position:absolute;inset:0}
  .brand{position:absolute;left:0;right:0;top:72px;display:flex;justify-content:center;align-items:center;gap:12px;
      color:var(--navy);font-family:"Montserrat",sans-serif;font-weight:800;font-size:30px;line-height:1;
      text-shadow:0 0 6px #fff,0 0 10px #fff}
  .brand__dot{width:22px;height:22px;border-radius:50%;background:var(--navy)}
  .headline{position:absolute;left:0;right:0;top:134px;text-align:center;color:var(--navy);
      font-family:"Montserrat",sans-serif;font-weight:800;font-size:74px;line-height:66px;
      text-shadow:0 0 6px #fff,0 0 10px #fff}
  .features{position:absolute;left:70px;right:70px;top:280px;display:flex;justify-content:space-between;list-style:none;
      font-family:"Fredoka",sans-serif;font-weight:600;font-size:21px;color:var(--navy-deep);
      text-shadow:0 0 3px #fff,0 0 3px #fff,0 0 5px #fff}
  .features__item{display:flex;align-items:center;gap:6px}
  .features__tick{width:22px;height:22px}
  .web{position:absolute;left:329px;top:332px;width:536px;height:59px;border-radius:30px;
      background:linear-gradient(180deg,var(--green-light),var(--green));display:flex;align-items:center;
      box-shadow:0 3px 6px rgba(0,0,0,.35);overflow:hidden}
  .web__icon{width:74px;height:100%;background:var(--pill-dark);display:flex;align-items:center;justify-content:center;border-radius:30px 0 0 30px}
  .web__url{flex:1;text-align:center;font-family:"Fredoka",sans-serif;font-weight:600;font-size:25px;color:var(--navy-deep)}
  .directions{position:absolute;left:210px;width:760px;top:416px;height:91px;display:flex;align-items:center;justify-content:center;
      font-family:"Lilita One",sans-serif;font-size:40px;color:var(--white);letter-spacing:.5px;
      text-shadow:2px 2px 0 var(--navy-deep),-1px -1px 0 #000}
  .open-badge{position:absolute;left:982px;top:22px;width:122px;height:72px}
  .open-badge__text{position:absolute;inset:0;text-align:center;font-family:"Oswald",sans-serif;font-weight:700;color:var(--white);transform:skewX(-10deg)}
  .open-badge__small{display:block;font-size:12px;line-height:14px}
  .open-badge__small--top{text-align:right;padding-right:10px;padding-top:3px}
  .open-badge__small--bottom{text-align:left;padding-left:14px}
  .open-badge__big{display:block;font-size:38px;line-height:38px}
</style>
</head>
<body>
<div class="billboard">
  <div class="billboard__photo" role="img" aria-label="Faded aerial photo of the storage facility with unit buildings, parked RVs and the road"></div>

  <svg class="billboard__shapes" width="1120" height="560" viewBox="0 0 1120 560">
    <defs>
      <linearGradient id="curlShade" x1="0" y1="0" x2="1" y2="1">
        <stop offset="0" stop-color="#ffffff"/>
        <stop offset="0.6" stop-color="#f2f2f2"/>
        <stop offset="1" stop-color="#b9b9b9"/>
      </linearGradient>
    </defs>
    <polygon class="corner-red" points="813,0 1120,0 1120,240" fill="var(--red)"/>
    <path class="corner-curl" d="M813,0 Q945,18 975,110 Q1005,205 1120,245 L1120,262 Q960,190 813,0 Z" fill="url(#curlShade)"/>
    <g class="direction-arrow" fill="var(--navy)">
      <polygon points="150,462 269,378 269,546"/>
      <rect x="266" y="416" width="705" height="91"/>
    </g>
    <path class="open-bubble" d="M982,20 L1106,20 L1106,94 L1056,94 L1042,116 L1040,94 L976,94 Z" fill="none" stroke="var(--green)" stroke-width="4"/>
  </svg>

  <div class="brand">
    <span class="brand__dot"></span>
    <span class="brand__name">SAM GREENFIELD SELF STORAGE</span>
  </div>

  <h1 class="headline">SELF STORAGE<br>SERVICES</h1>

  <ul class="features">
    <li class="features__item"><svg class="features__tick" viewBox="0 0 24 24"><circle cx="12" cy="12" r="10" fill="none" stroke="var(--green)" stroke-width="2.5"/><path d="M7 12.5l3.5 3.5 7-8" fill="none" stroke="var(--green)" stroke-width="3" stroke-linecap="round" stroke-linejoin="round"/></svg>LARGE / SMALL UNITS</li>
    <li class="features__item"><svg class="features__tick" viewBox="0 0 24 24"><circle cx="12" cy="12" r="10" fill="none" stroke="var(--green)" stroke-width="2.5"/><path d="M7 12.5l3.5 3.5 7-8" fill="none" stroke="var(--green)" stroke-width="3" stroke-linecap="round" stroke-linejoin="round"/></svg>TEMPERATURE CONTROLLED</li>
    <li class="features__item"><svg class="features__tick" viewBox="0 0 24 24"><circle cx="12" cy="12" r="10" fill="none" stroke="var(--green)" stroke-width="2.5"/><path d="M7 12.5l3.5 3.5 7-8" fill="none" stroke="var(--green)" stroke-width="3" stroke-linecap="round" stroke-linejoin="round"/></svg>COVERED BOAT / RV PARKING</li>
  </ul>

  <div class="web">
    <div class="web__icon">
      <svg width="40" height="40" viewBox="0 0 40 40" fill="none" stroke="#fff" stroke-width="2.5">
        <circle cx="18" cy="18" r="13"/><ellipse cx="18" cy="18" rx="6" ry="13"/><line x1="5" y1="18" x2="31" y2="18"/><line x1="7" y1="11" x2="29" y2="11"/><line x1="7" y1="25" x2="29" y2="25"/>
        <path d="M25 24 L36 29 L31 31 L34 37 L31 38 L28 32 L25 35 Z" fill="#fff" stroke="var(--pill-dark)" stroke-width="1.5"/>
      </svg>
    </div>
    <span class="web__url">WWW.HARBORSTORAGEGROUP.COM</span>
  </div>

  <div class="directions">214 MAPLE RIDGE DRIVE | 555-014-2736</div>

  <div class="open-badge">
    <div class="open-badge__text">
      <span class="open-badge__small open-badge__small--top">ALWAYS</span>
      <span class="open-badge__big">OPEN</span>
      <span class="open-badge__small open-badge__small--bottom">ONLINE!</span>
    </div>
  </div>
</div>
</body>
</html>
```